Briefkopf und Visitenkarte für Kanzlei
Zielgruppe
Wir sind eine Kanzlei mit Sitz in Neuss und den Schwerpunkten im Arbeitsrecht und Strafrecht. Unser Rechtsanwalt Kerem Yalçıntaş ist zugleich Fachanwalt für das Arbeitsrecht. Unsere Zielgruppe sind alle Menschen, die in diesen beiden Gebieten Rechtsberatung oder Vertretung suchen. Nähere Informationen über uns findet Ihr auf www.hovbera-kanzlei.de
Aufgabenstellung
Was ich möchte:
- das Design sollte schlicht sein und nicht zu dick auftragen. Zu schlicht ist aber auch nicht gut, schlielich soll erkennbar sein, dass die Briefvorlage nicht von einem Laien ertellt wurde, sondern von einem Designer.
- Farbakzente wie marineblau und gold sind gewünscht, allerdings nicht zu übertrieben, weil das sonst vom Textinhalt ablenkt und zu viel Tinte verbraucht.
- Der Briefkopf sollte folgende Informationen anzeigen: Fachanwaltstitel, Anschrift, Kontaktmöglichkeiten wie Telefon, Fax, E-Mail und Webseite, Öffnungszeiten, Bankverbindung und Umsatzsteuer IDNr.
- Eine Kopfzeile oder Fußzeile mit dem Kanzleinamen - / Logo, die auch ab Seite 1. weitergeführt wird.
- Die Seitenzahl sollte ersichtlich sein.
- Die Endddatei sollte hinsichtlich der angegebenen Daten (wie bspw. Telefonnummer und Anschrift) leicht veränderbar sein (gewünscht sind word und rtf als Dateiformat)
- Die Schriftart für den Schriftzug Halls Of Falcons ist Trajan pro.
Was ich nicht möchte:
- Keine Wasserzeichen in der Mitte des Textes. Das lenkt von der Schrift ab.
- Die Enddatei sollte nicht groß sein (idealerweise unter 0,75 -1 mb), da wir unsere Schreiben oft per Mail versenden und der Anhang dadurch zu groß würde.

```html
<!DOCTYPE html>
<html lang="de">
<head>
<meta charset="utf-8">
<title>Halls of Falcons – Briefbogen</title>
<link href="https://fonts.googleapis.com/css2?family=Cinzel:wght@400;700&family=Source+Sans+3:wght@400;700&display=swap" rel="stylesheet">
<style>
  :root {
    --navy: #0066b3;
    --gold: #a8915f;
    --ink: #1a1a1a;
    --paper: #ffffff;
  }
  html, body { margin: 0; padding: 0; overflow: hidden; background: var(--paper); }
  .letter {
    position: relative; width: 848px; height: 1200px; overflow: hidden;
    background: var(--paper); color: var(--ink);
    font-family: "Source Sans 3", sans-serif;
  }
  .top-band { position: absolute; top: 0; left: 0; width: 100%; height: 20px; background: var(--navy); }
  .brand-mark { position: absolute; left: 371px; top: 53px; }
  .brand-name {
    position: absolute; left: 500px; top: 78px; width: 302px; text-align: center;
    font-family: "Cinzel", serif; font-variant: small-caps; color: var(--navy);
    font-size: 28px; line-height: 30px; letter-spacing: 0.5px;
  }
  .brand-tagline {
    position: absolute; left: 500px; top: 110px; width: 302px; text-align: center;
    font-family: "Cinzel", serif; color: var(--gold); font-size: 12.5px; letter-spacing: 0.6px;
  }
  .return-line {
    position: absolute; left: 81px; top: 222px; white-space: nowrap;
    font-weight: 700; font-size: 11px; color: var(--navy); letter-spacing: 0.5px;
  }
  .recipient { position: absolute; left: 81px; top: 256px; font-size: 15.5px; line-height: 19px; font-style: normal; letter-spacing: 0.2px; }
  .recipient .city { margin-top: 18px; }
  .sidebar {
    position: absolute; left: 622px; top: 213px; width: 210px;
    font-family: "Cinzel", serif; font-size: 9px; line-height: 12.6px; color: var(--navy);
  }
  .sidebar .firm { color: var(--gold); font-variant: small-caps; font-size: 9.5px; }
  .sidebar .block { margin-bottom: 12.6px; }
  .sidebar .lawyer { font-weight: 700; font-variant: small-caps; font-size: 9.5px; }
  .sidebar .addr { font-variant: small-caps; font-size: 9.5px; }
  .contact { display: grid; grid-template-columns: 51px 1fr; margin: 0; }
  .contact dt { font-weight: 700; margin: 0; }
  .contact dd { margin: 0; font-size: 8px; white-space: nowrap; }
  .body-text {
    position: absolute; left: 81px; top: 479px; width: 509px;
    font-size: 16px; line-height: 17.1px; text-align: justify; letter-spacing: 0.25px;
  }
  .body-text p { margin: 0 0 17.1px; }
  .closing { position: absolute; left: 81px; top: 990px; font-size: 13.5px; }
  .footer {
    position: absolute; left: 0; width: 100%; text-align: center; white-space: nowrap;
    font-family: "Cinzel", serif; font-variant: small-caps; color: var(--navy);
  }
  .footer-name { top: 1129px; font-size: 13px; }
  .footer-hours { top: 1155px; font-size: 12.5px; }
  .footer-bank { top: 1169px; left: 4px; font-size: 12.5px; letter-spacing: 0.5px; }
</style>
</head>
<body>
<main class="letter">
  <div class="top-band"></div>

  <svg class="brand-mark" width="106" height="106" viewBox="0 0 106 106" aria-hidden="true">
    <defs>
      <linearGradient id="goldTone" x1="0" y1="0" x2="1" y2="1">
        <stop offset="0" stop-color="#d8c594"/>
        <stop offset="1" stop-color="#a08a58"/>
      </linearGradient>
    </defs>
    <circle cx="53" cy="53" r="52" fill="url(#goldTone)"/>
  </svg>
  <div class="brand-name">Halls of Falcons</div>
  <div class="brand-tagline">ANWALT FÜR STRAF UND ARBEITSRECHT</div>

  <div class="return-line">HALLS OF FALCONS • FALKENWEG 8 • 47199 RHEINBRÜCK</div>

  <address class="recipient">
    <div>Max Mustermann</div>
    <div>Musterstraße 1</div>
    <div class="city">12345 Musterstadt</div>
  </address>

  <aside class="sidebar">
    <div class="block firm">Halls of Falcons<br>Anwalt für Straf und Arbeitsrecht</div>
    <div class="block">
      <div class="lawyer">Kerem Yalçıntaş</div>
      <div class="addr">Falkenweg 8</div>
      <div class="addr">47199 Rheinbrück</div>
    </div>
    <dl class="contact">
      <dt>TEL:</dt><dd>0123 48 70 210</dd>
      <dt>FAX:</dt><dd>0123 48 70 211</dd>
      <dt>MAIL:</dt><dd>KONTAKT@HOVBERA-KANZLEI.DE</dd>
      <dt>WEB:</dt><dd>WWW.HOVBERA-KANZLEI.DE</dd>
    </dl>
  </aside>

  <section class="body-text">
    <p>Sehr geehrter Klient,</p>
    <p>Luptasped quatincia ipitem volupta as etumenia voluptat maximus dignis venim corit, cupiet optas nobitem quatem velectorum faccae inverit aligeni sitioribus adit, sequodi genisse nimilli tianda con nost vollabo. Atatent pratempore venditasped utamus duci comniti busdam cum doluptat.<br>Torepudam es vit fugiametur re, voluptatur si derum ut omnimus ma vollis modigenient aut quunt volore im sandaerovit, se dolenes quis autesciatem consed quibus.</p>
    <p>Bus sit venduci digendit vidit ea ipsandi consequam intiste stibusam ide ni con por simus, occatus quat parchillab inulparum nones sequi tetur a aut unt quissimusam et ut imilla nem voluptum unt volorat faceptatus ant a quas sae quo occullo rehendiam repedit adi nis aut et aut ut utendus ex explici dessit is in eium hil idusam et officias accusaped que cus ea sam que cuptiossus sequas remquaecte cum aute volo et moluptatur am, quo cum haria quatum sitate vollit quid et aperferum quatum imaximinctem doluptatio omnime nest que rerati ute nuste solorum fugitiu ntempostium dolore eum rerferi nonsequ asiminc ipitas quam facest audanditati utemquam re, nonsedi tiisciendia seque nonsequis veni dolupta epellorem es idel ma est, te quibus et estrunt qui asperum faccus.</p>
    <p>Omniscient odipsusamus exerovi duntia is et il iliqui optatquae pra cus alibusam sequodi onsequat. Vit a dolo ilit volut quamenest eum nonet utatumet labore as asperro maionet ea endis eumqui as magnam imolum autest et quam aceaqua eperem et, imus est hiciis as dollestis dollorepedis sus, odiorendi nam eos explit harunt ulpa non re idellenes a doluptio.</p>
  </section>

  <div class="closing">Mit freundlichen Grüßen</div>

  <footer>
    <div class="footer footer-name">Halls of Falcons</div>
    <div class="footer footer-hours">Öffnungszeiten: Mo-Fr. 08:30 - 13:00 und 14:00 - 17:00</div>
    <div class="footer footer-bank">Bankverbindung: Rheinische Kreditbank | DE44 3005 0110 0087 6543 21 | BIC: RHKRDEDDXXX | USt-ID-Nr. DE318406275</div>
  </footer>
</main>
</body>
</html>
```